Brastmoor "Past The Ridge" Single Album Artwork

Brastmoor is a hard rock / metal band that are releasing two singles and a full album. The two singles and album will have each their own album cover artwork. Of course as any rock or metal band we like a more rock n roll look when it comes to graphic arts.

Past the ridge is a song that we need an album cover for and we have a faint idea of what could be the cover but we have no idea how hard it could be to make. Essentially we want the cover to be us 4 band members standing on a cliff under a glazing sun. The issue we have is we don't have a photo of us standing on a cliff, instead we have a photo of us four together on sand (see below) Unsure if this design is possible we hope that one designer is talented enough to be able to complete our request. Otherwise as always, any entrepreneurial designers can send in a design they think may be better.

The band is a rock / metal band so it has to look like a rock / metal band cover - just keep that in mind.

```html
<!DOCTYPE html>
<html lang="en">
<head>
<meta charset="UTF-8">
<title>Brastmoor – Past The Ridge</title>
<link rel="stylesheet" href="https://fonts.googleapis.com/css2?family=Anton&family=Black+Ops+One&display=swap">
<style>
  :root {
    --sky-light: #f1ece2;
    --sky-haze: #ddd2bf;
    --horizon: #b7a385;
    --valley: #9c8468;
    --cliff-top: #7a624b;
    --cliff-dark: #4a3b2d;
    --band-shade: #5a4a3b;
    --title-ink: #231f1b;
    --band-fill: #c9b394;
  }
  html, body {
    margin: 0;
    padding: 0;
    width: 1200px;
    height: 1200px;
    overflow: hidden;
    background: var(--sky-light);
  }
  .cover {
    position: relative;
    width: 1200px;
    height: 1200px;
    overflow: hidden;
  }
  .cover-sky {
    position: absolute;
    inset: 0;
    background:
      radial-gradient(circle at 48% 44%, rgba(255, 250, 236, 0.9) 0, rgba(255, 250, 236, 0) 30%),
      linear-gradient(180deg, var(--sky-light) 0%, var(--sky-haze) 38%, var(--horizon) 48%, var(--valley) 75%, #7f6a54 100%);
  }
  .cover-cliff {
    position: absolute;
    left: 0;
    top: 450px;
    width: 760px;
    height: 750px;
    border-radius: 0 120px 0 0;
    background: linear-gradient(180deg, var(--cliff-top) 0%, #6a5542 45%, var(--cliff-dark) 100%);
  }
  .cover-band {
    position: absolute;
    left: 30px;
    top: 150px;
    width: 540px;
    height: 370px;
    border-radius: 10px;
    background: linear-gradient(180deg, rgba(90, 74, 59, 0.55) 0%, rgba(90, 74, 59, 0.8) 100%);
  }
  .cover-type {
    position: absolute;
    inset: 0;
    width: 1200px;
    height: 1200px;
  }
  .single-title {
    font-family: "Black Ops One", "Impact", sans-serif;
    font-size: 62px;
    fill: var(--title-ink);
  }
  .band-name {
    font-family: "Anton", "Impact", sans-serif;
    font-size: 340px;
    fill: var(--band-fill);
    fill-opacity: 0.8;
  }
</style>
</head>
<body>
  <main class="cover">
    <div class="cover-sky" role="img" aria-label="Hazy sepia sky and valley under a glaring sun"></div>
    <div class="cover-cliff" role="img" aria-label="Rocky cliff edge in warm brown tones"></div>
    <div class="cover-band" role="img" aria-label="Four band members standing on the cliff edge, backlit by the sun"></div>
    <svg class="cover-type" viewBox="0 0 1200 1200">
      <text class="single-title" x="715" y="406" textLength="445" lengthAdjust="spacingAndGlyphs">PAST THE RIDGE</text>
      <text class="band-name" x="48" y="1090" textLength="1077" lengthAdjust="spacingAndGlyphs">BRASTMOOR</text>
    </svg>
  </main>
</body>
</html>
```